New Startup IT services website

We are looking for a designer to design and create a ‘child worpress’ design based on the pixelmarket-4820317-lumina-responsive-wordpress-theme (http://pixelmarket-example.net/item/lumina-responsive-wordpress-theme/4820317) . We have previously purchased this. We are looking for a front page and sub page design and coding.

That said, if you have a theme you believe would better suit our needs we are open to suggestions.

brightlinqIT is a start-up IT company whose vision is ‘To be the trusted technology service provider of choice for every business in the health industry in SEQ.’

We are focusing on the health sector by which we mean – doctors, dentists, physiotherapists, chiropractors, natural and alternative medicine, radiology, pathology, specialists etc

Please see the attached images for our logo and business card design for colour ideas etc. This website should have a professional focus. Please see the slider below.

Target Market(s)

doctors, dentists, physiotherapists, chiropractors, natural and alternative medicine, radiology, pathology, specialists etc

Requirements
Must have
• The front page elements should include the following :-
• Menu Structure will consist of
• HOME / OUR APPROACH / SERVICES / PARTNERS / FAQ / CONTACT US
• ------------------
• Menu Slider (picture window)
• Design (with images) the following 4 graphics and text
• 1. After Hours approach – We do our work, when you’re not doing yours.
• 2. FREE 32 point checklist – How reliable is your technology really?
• 3. We Specialize in Security and protecting your patients confidentiality
• 4. The Cloud – Buzzword or the future? Ask us what you can and can’t do with it.
• -------------------
• 3 FEATURES
• Here we want a section where we show three major features of our company. These are just a snapshot which will link to background pages. The three areas are:
• 1. Complete Services – What we offer
• 2. New Practise – We specialise in setting up new medical practises.
• 3. Our Approach / unique / we do our work, when you’re not doing yours.
• -------------------
• We would like a small text area (no more than 100 words) for us to introduce brightlinkIT as a services company.
• -------------------
• Partners Logos – A small area on the front screen page where we can promote the major partners we work with. Will Also link to Partners Page
• -------------------
• Footer
• To include site map, privacy policy, ABN (which is an Australian business number) copyright message

```html
<!DOCTYPE html>
<html lang="en">
<head>
<meta charset="utf-8">
<title>Brightlink IT</title>
<link rel="stylesheet" href="https://fonts.googleapis.com/css2?family=Ubuntu:wght@400;500&family=Open+Sans:wght@400;600&family=Noto+Serif:ital@1&display=swap">
<style>
:root{
  --navy:#1d3f7a;
  --blue:#2a5aa6;
  --sky:#1f6fb5;
  --orange:#f28c1a;
  --text:#555b66;
  --muted:#8a93a6;
  --line:#dde1e8;
  --footer-top:#3f5fa6;
  --footer-bot:#24418a;
  --bar:#223f86;
  --white:#fff;
}
*{margin:0;padding:0;box-sizing:border-box}
html,body{width:733px;height:1200px;overflow:hidden;background:var(--white)}
body{position:relative;font-family:"Open Sans",Arial,sans-serif;color:var(--text)}
.abs{position:absolute}
/* header */
.header{left:0;top:0;width:733px;height:90px;border-bottom:1px solid #eceef2}
.brand{left:50px;top:34px;font-family:"Ubuntu",sans-serif;font-weight:500;font-size:27px;color:var(--sky);display:flex;align-items:center;gap:6px;letter-spacing:-.5px}
.brand-dot{width:9px;height:9px;border-radius:50%;background:var(--orange)}
.phone{right:40px;top:18px;font-family:"Ubuntu",sans-serif;font-size:15px;color:var(--orange)}
.nav{left:317px;top:46px;display:flex;align-items:center;font-family:"Ubuntu",sans-serif;font-size:10px;color:#4a5160}
.nav a{color:inherit;text-decoration:none;padding:0 9px;border-left:1px solid #c8ccd4;line-height:11px}
.nav a.active{background:linear-gradient(#2676c4,#1456a0);color:#fff;height:24px;line-height:24px;padding:0 14px;border:none;border-radius:2px;margin-right:3px}
.nav a.active + a{border-left:none}
/* hero */
.hero{left:0;top:90px;width:733px;height:264px;background:linear-gradient(#fff 0%,#f6f8fb 60%,#eef1f6 100%)}
.hero-sub{left:48px;top:150px;font-family:"Ubuntu",sans-serif;font-size:18px;color:var(--sky)}
.hero-title{left:48px;top:172px;font-family:"Ubuntu",sans-serif;font-weight:500;font-size:29px;color:var(--navy)}
.hero-text{left:48px;top:211px;width:300px;font-size:9.5px;line-height:16px;color:var(--muted)}
.dots{left:50px;top:252px;display:flex;gap:3px}
.dots span{width:9px;height:9px;border-radius:50%;background:#7cc0ea}
.dots span:first-child{background:var(--orange)}
.hero-art{left:436px;top:108px;width:180px;height:200px;border-radius:6px;background:radial-gradient(circle at 50% 40%,#f4f5f7,#d9dce2 70%,#eef0f4)}
/* intro */
.intro-title{left:42px;top:384px;font-family:"Ubuntu",sans-serif;font-size:16px;color:#333}
.intro-lead{left:42px;top:410px;width:300px;font-size:10px;line-height:16px;color:var(--blue)}
.intro-body{left:42px;top:445px;width:290px;font-size:8.3px;line-height:14.4px;color:var(--text)}
.intro-body p+p{margin-top:4px}
.card-img{top:382px;width:154px;height:78px}
.img-a{left:366px;background:linear-gradient(135deg,#e9eef3,#b9c6d3)}
.img-b{left:543px;background:linear-gradient(135deg,#9cc5ea,#e3edf6)}
.card-title{top:467px;font-family:"Ubuntu",sans-serif;font-size:10.5px;color:var(--navy)}
.card-text{top:485px;width:155px;font-size:8.3px;line-height:14.4px;color:var(--text)}
/* quote */
.rule{left:34px;width:666px;height:1px;background:var(--line)}
.quote{left:74px;top:579px;width:600px;font-family:"Noto Serif",serif;font-style:italic;font-size:12.5px;line-height:20px;color:#7e8aa3}
.qmark{font-style:normal;font-size:24px;color:#8a97b3;font-family:Georgia,serif;vertical-align:-6px}
/* services */
.service{width:208px;height:103px;border:1px solid #d6d9df;border-radius:2px;background:#fff}
.service svg{position:absolute;left:10px;top:12px}
.service h3{position:absolute;left:43px;top:12px;font-family:"Ubuntu",sans-serif;font-weight:400;font-size:12.5px;color:var(--orange)}
.service p{position:absolute;left:43px;top:33px;width:158px;font-size:8.3px;line-height:14.4px;color:var(--text)}
/* partners */
.partners{left:0;top:906px;width:733px;height:62px;display:flex;justify-content:space-around;align-items:center;padding:0 40px;font-family:"Ubuntu",sans-serif;font-weight:500;font-size:16px;color:#1f4b93;letter-spacing:1px}
/* footer */
.footer{left:0;top:968px;width:733px;height:184px;background:linear-gradient(var(--footer-top),var(--footer-bot));color:#dfe6f5}
.fcol{top:28px;font-size:8.3px;line-height:15px}
.fcol h4{font-family:"Ubuntu",sans-serif;font-weight:400;font-size:13.5px;color:#fff;margin-bottom:10px;line-height:16px}
.fcol .org{font-family:"Ubuntu",sans-serif;font-size:11px;color:#fff;line-height:14px;margin-bottom:2px}
.fcol .date{color:#fff}
.social{display:flex;gap:4px;margin-top:10px}
.social span{width:17px;height:17px;border-radius:50%;background:#fff}
.bottom{left:0;top:1152px;width:733px;height:48px;background:var(--bar);font-size:8.3px;color:#dfe6f5}
.copy{left:42px;top:18px}
.legal{right:60px;top:18px;color:#fff}
</style>
</head>
<body>
<header class="abs header">
  <div class="abs brand"><span>brightlinkIT</span><span class="brand-dot"></span></div>
  <div class="abs phone">(07) 5550 1234</div>
  <nav class="abs nav">
    <a class="active" href="#">HOME</a><a href="#">OUR APPROACH</a><a href="#">SERVICES</a><a href="#">PARTNERS</a><a href="#">FAQ</a><a href="#">CONTACT US</a>
  </nav>
</header>

<section class="abs hero"></section>
<div class="abs hero-sub">Protecting your patients confidentiality</div>
<h1 class="abs hero-title">We Specialize in Security</h1>
<p class="abs hero-text">Mauris vel lacus vitae felis vestibulum volutpat Etiam est nunc venenatis in tristique eu imperdiet ac nisl</p>
<div class="abs dots"><span></span><span></span><span></span><span></span></div>
<div class="abs hero-art" role="img" aria-label="Illustration of a doctor figure with a first-aid case emerging from a laptop"></div>

<h2 class="abs intro-title">What is Brightlink IT ?</h2>
<p class="abs intro-lead">Vivamus porttitor, g, purus nisi eleifend libero, a tempus libero lectus feugiat felis Morbi diam mauris</p>
<div class="abs intro-body">
  <p>Morbi eget arcu. Morbi porta, libero id ullamcorper nonummy, nibh ligula pulvinar metus, eget consectetuer augue nisi quis lacus. Ut ac mi quis lacus mollis aliquam. Curabitur iaculis tempus eros. Curabitur vel mi sit amet magna malesuada ultrices. Ut nisi erat, fermentum vel, congue id.</p>
  <p>Euismod in, elit. Fusce ultricies, orci ac feugiat suscipit, leo massa sodales velit, et scelerisque mi tortor at ipsum</p>
</div>
<div class="abs card-img img-a" role="img" aria-label="Photo of medical imaging equipment"></div>
<div class="abs card-img img-b" role="img" aria-label="Photo of smiling medical staff in a clinic"></div>
<h3 class="abs card-title" style="left:366px">HOW WE WORK</h3>
<h3 class="abs card-title" style="left:547px">WHAT WE DO</h3>
<p class="abs card-text" style="left:366px">Euismod in, elit. Fusce ultricies, orci ac feugiat suscipit, leo massa sodales velit, et scelerisque mi tortor at ipsum</p>
<p class="abs card-text" style="left:547px">Euismod in, elit. Fusce ultricies, orci ac feugiat suscipit, leo massa sodales velit, et scelerisque mi tortor at ipsum</p>

<div class="abs rule" style="top:563px"></div>
<blockquote class="abs quote"><span class="qmark">&#8220;</span> Mauris vel lacus vitae felis vestibulum volutpat Etiam est nunc venenatis in tristique eu imperdiet ac nisl Cum sociis natoque penatibus et magnis dis parturient montes, <span class="qmark">&#8221;</span></blockquote>
<div class="abs rule" style="top:641px"></div>

<div class="abs service" style="left:34px;top:662px">
  <svg width="28" height="24" viewBox="0 0 28 24"><path d="M1 13h7l3-9 4 17 3-10h9" fill="none" stroke="#f28c1a" stroke-width="2" stroke-linejoin="round"/></svg>
  <h3>Featured Service</h3><p>Mauris vel lacus vitae felis vestibulum volutpat. Etiam est nunc, venenatis in, tristique eu, imperdiet ac, nisl. Cum sociis natoque penatibus et magnis</p>
</div>
<div class="abs service" style="left:258px;top:662px">
  <svg width="28" height="26" viewBox="0 0 28 26"><circle cx="14" cy="7" r="6" fill="#f28c1a"/><path d="M2 26c0-8 5-12 12-12s12 4 12 12z" fill="#f28c1a"/></svg>
  <h3>Featured Service</h3><p>Mauris vel lacus vitae felis vestibulum volutpat. Etiam est nunc, venenatis in, tristique eu, imperdiet ac, nisl. Cum sociis natoque penatibus et magnis</p>
</div>
<div class="abs service" style="left:482px;top:662px">
  <svg width="28" height="24" viewBox="0 0 28 24"><path d="M3 12c4-8 14-9 22-7-3 8-12 11-22 7z" fill="#f28c1a"/><path d="M14 11v12" stroke="#f28c1a" stroke-width="2"/></svg>
  <h3>Featured Service</h3><p>Mauris vel lacus vitae felis vestibulum volutpat. Etiam est nunc, venenatis in, tristique eu, imperdiet ac, nisl. Cum sociis natoque penatibus et magnis</p>
</div>
<div class="abs service" style="left:34px;top:776px">
  <svg width="28" height="30" viewBox="0 0 28 30"><path d="M14 2c-5 0-7 3-7 6s2 6 4 9L4 27l4 2 6-9 6 9 4-2-7-10c2-3 4-6 4-9s-2-6-7-6zm0 4c2 0 3 1 3 2s-1 3-3 5c-2-2-3-4-3-5s1-2 3-2z" fill="#f28c1a"/></svg>
  <h3>Featured Service</h3><p>Mauris vel lacus vitae felis vestibulum volutpat. Etiam est nunc, venenatis in, tristique eu, imperdiet ac, nisl. Cum sociis natoque penatibus et magnis</p>
</div>
<div class="abs service" style="left:258px;top:776px">
  <svg width="28" height="28" viewBox="0 0 28 28"><rect x="1" y="1" width="26" height="26" rx="3" fill="#f28c1a"/><path d="M14 7v14M7 14h14" stroke="#fff" stroke-width="3.5"/></svg>
  <h3>Featured Service</h3><p>Mauris vel lacus vitae felis vestibulum volutpat. Etiam est nunc, venenatis in, tristique eu, imperdiet ac, nisl. Cum sociis natoque penatibus et magnis</p>
</div>
<div class="abs service" style="left:482px;top:776px">
  <svg width="28" height="28" viewBox="0 0 28 28"><g transform="rotate(45 14 14)"><rect x="10" y="0" width="8" height="26" rx="4" fill="none" stroke="#f28c1a" stroke-width="2"/><path d="M10 15h8v7a4 4 0 0 1-8 0z" fill="#f28c1a"/></g></svg>
  <h3>Featured Service</h3><p>Mauris vel lacus vitae felis vestibulum volutpat. Etiam est nunc, venenatis in, tristique eu, imperdiet ac, nisl. Cum sociis natoque penatibus et magnis</p>
</div>

<div class="abs partners">
  <span>Corvex</span><span>Nimbra</span><span>Altoria</span><span>Kestrel</span><span>Veyra</span><span>Ondrix</span>
</div>

<footer class="abs footer">
  <div class="abs fcol" style="left:42px">
    <h4>Contact Information</h4>
    <div class="org">Brightlink IT</div>
    42 Harbour Lane, Suite 3<br>Springfield 4021 QLD<br>Phone no. (07) 5550 1234<br>Fax: 0400 000 111<br>Email: hello@brightlinkit.example
  </div>
  <div class="abs fcol" style="left:205px;width:180px">
    <h4>Recent Blog Post</h4>
    <div class="date">20/Sept/2013</div>Vivamus porttitor purus nisi eleifend<br><br>
    <div class="date">17/Sept/2013</div>Libero tempus libero lectus feugiat felis diam mauris viverra in, gravida eu
  </div>
  <div class="abs fcol" style="left:415px;line-height:18.4px">
    <h4 style="margin-bottom:6px">Usefull links</h4>
    Phasellus felis dolor<br>Scelerisque tempus eget<br>Lobortis id libero<br>Donec scelerisque<br>Praesent sit amet est
  </div>
  <div class="abs fcol" style="left:556px;width:150px">
    <h4>Get Connected</h4>
    You can contact us via email button below or submit online FORM &rarr;
    <div class="social"><span></span><span></span><span></span><span></span></div>
  </div>
</footer>
<div class="abs bottom">
  <div class="abs copy">&copy; 2013 Company Name.&nbsp; All right reserved.&nbsp; Term of Use</div>
  <div class="abs legal">Sitemap &nbsp;|&nbsp; Privacy policy</div>
</div>
</body>
</html>
```